Modernization of our corporate website

The goal of this task is to propose a new template for our website, http://vlomk.fr/

We just made a new batch of business cards (see attachments) and the new website has to match them.

Feel free to request current HTML.

```html
<!DOCTYPE html>
<html lang="fr">
<head>
<meta charset="utf-8">
<title>vlomk . Hosting Architects — Hebergement</title>
<link rel="stylesheet" href="https://fonts.googleapis.com/css2?family=Carlito:wght@400;700&family=Open+Sans:wght@400&display=swap">
<style>
  :root {
    --bg: #efefef;
    --bg-light: #fbfbfb;
    --ink: #111;
    --muted: #8a8a8a;
    --rule: #c9c9c9;
    --blue: #2a2aff;
    --red: #ff1744;
    --magenta: #ff2bd6;
    --cyan: #2ee6e6;
    --green: #33e633;
    --yellow: #ffe21a;
    --lavender: #8c8cff;
    --lime: #8cff3a;
  }
  * { margin: 0; padding: 0; box-sizing: border-box; }
  html, body { width: 1200px; height: 762px; overflow: hidden; }
  body {
    position: relative;
    font-family: "Carlito", "Calibri", sans-serif;
    color: var(--ink);
    background: radial-gradient(circle at 220px 170px, #fff 0, #f6f6f6 140px, var(--bg) 420px), var(--bg);
  }
  .backdrop { position: absolute; inset: 0; z-index: 0; }
  .page { position: relative; z-index: 1; }

  .site-title {
    position: absolute; top: 38px; left: 0; width: 1200px;
    text-align: center; font-family: "Open Sans", sans-serif;
    font-weight: 400; font-size: 43px; letter-spacing: 0.3px;
  }
  .main-nav {
    position: absolute; top: 96px; left: 0; width: 1200px;
    display: flex; justify-content: center; gap: 9px;
    font-size: 19px;
  }
  .nav-item { border-left: 2px solid; padding-left: 7px; line-height: 20px; color: var(--ink); text-decoration: none; }
  .nav-item.blue { border-color: var(--blue); }
  .nav-item.red { border-color: var(--red); }
  .nav-item.magenta { border-color: var(--magenta); }
  .nav-item.cyan { border-color: var(--cyan); }
  .nav-item.green { border-color: var(--green); }

  .page-title {
    position: absolute; top: 194px; left: 427px;
    display: flex; align-items: center;
    font-family: "Open Sans", sans-serif; font-weight: 400; font-size: 52px; line-height: 56px;
  }
  .page-title::before {
    content: ""; width: 9px; height: 49px; background: var(--red);
    border-radius: 2px; margin-right: 2px;
  }

  .content { position: absolute; top: 343px; left: 135px; width: 935px; font-size: 19px; line-height: 24px; }
  .content ul { margin: 20px 0 20px 40px; }
  .content li { padding-left: 0; }

  .footer-nav {
    position: absolute; top: 602px; left: 0; width: 1200px;
    display: flex; justify-content: center; gap: 8px;
    font-size: 17px; font-weight: 700; color: var(--muted);
  }
  .footer-nav .nav-item { color: var(--muted); line-height: 18px; }
  .footer-nav .yellow { border-color: var(--yellow); }
  .footer-nav .lavender { border-color: var(--lavender); }
  .footer-nav .lime { border-color: var(--lime); }

  .footer-rule { position: absolute; top: 645px; left: 135px; width: 935px; height: 2px; background: var(--rule); }
  .legal {
    position: absolute; top: 656px; left: 0; width: 1200px;
    text-align: center; font-size: 14px; line-height: 15px; color: var(--muted);
  }
  .social-mark {
    position: absolute; top: 652px; left: 1000px; width: 50px; height: 50px;
    border-radius: 50%; background: #cfcfcf;
  }
</style>
</head>
<body>
  <svg class="backdrop" width="1200" height="762" viewBox="0 0 1200 762" aria-hidden="true">
    <defs>
      <linearGradient id="sweep" x1="0" y1="0" x2="1" y2="1">
        <stop offset="0" stop-color="#ffffff" stop-opacity="0.95"/>
        <stop offset="1" stop-color="#f2f2f2" stop-opacity="0.3"/>
      </linearGradient>
    </defs>
    <path d="M805 0 C 840 120, 760 230, 600 300 C 820 280, 1050 200, 1200 120 L1200 0 Z" fill="url(#sweep)"/>
  </svg>

  <div class="page">
    <h1 class="site-title">vlomk . Hosting Architects</h1>
    <nav class="main-nav">
      <a class="nav-item blue" href="#">accueil</a>
      <a class="nav-item red" href="#">Hebergement</a>
      <a class="nav-item magenta" href="#">ERP on a drive</a>
      <a class="nav-item cyan" href="#">Nano CDN</a>
      <a class="nav-item green" href="#">Etudes de cas</a>
    </nav>

    <h2 class="page-title">Hebergement</h2>

    <section class="content">
      <p>Nous proposons une gamme complète de service d'hébergement :</p>
      <ul>
        <li>Conception de plateforme</li>
        <li>Implémentation</li>
        <li>Hébergement par nos soins (voir nos études de cas et notre infrastructure)</li>
        <li>Gestion à distance de plateformes hébergées in-situ</li>
        <li>Infogérance totale ou partielle</li>
      </ul>
      <p>Nos prestations vont du simple hébergement d'un site Internet à l'hébergement et infogérance complète de plateformes complexes (ERP par exemple).</p>
    </section>

    <nav class="footer-nav">
      <a class="nav-item yellow" href="#">L'infrastructure</a>
      <a class="nav-item lavender" href="#">La société</a>
      <a class="nav-item lime" href="#">Contact</a>
    </nav>
    <div class="footer-rule"></div>
    <footer class="legal">
      <p>27 rue des Tilleuls - 75011 Paris - France</p>
      <p>RCS Paris B 482 519 604 (00027)</p>
    </footer>
    <div class="social-mark" aria-hidden="true"></div>
  </div>
</body>
</html>
```